Margot Vallis Designs

- Interior design consultant
- Want a monogram/logo at the top within a circle similar to quillantstudio.com.au
- Want the colors, font, theme, layout to be similar to quillantstudio.com.au
- Monogram possibly in the gold circle/leaf thing as visible on the attached pictures, maybe a MV with a backwards "E" within a circle
- Black background, white writing
- 1 side an enlarge logo with nothing else, other side to have a small logo at top with company name, mobile and email below

Industry/Entity Type

It Company

Contact Information for Business Card

Company name: Margot Vallis Interiors
Mobile: 0481 356 719
Email: margotvallis@postlark.com

Colors
000000
ffffff

```html
<!DOCTYPE html>
<html lang="en">
<head>
<meta charset="UTF-8">
<title>Margot Vallis Interiors — Business Card</title>
<link href="https://fonts.googleapis.com/css2?family=Pinyon+Script&family=Tinos&display=swap" rel="stylesheet">
<style>
  :root {
    --card-black: #000000;
    --ink-white: #ffffff;
    --backdrop: #ffffff;
    --frame-grey: #d9d9d9;
    --card-shadow: rgba(0, 0, 0, 0.18);
  }
  * { margin: 0; padding: 0; box-sizing: border-box; }
  html, body {
    width: 1200px;
    height: 1000px;
    overflow: hidden;
    background: var(--backdrop);
  }
  .canvas {
    width: 1200px;
    height: 1000px;
    display: flex;
    flex-direction: column;
    align-items: center;
    justify-content: center;
    gap: 40px;
  }
  .card {
    position: relative;
    width: 700px;
    height: 400px;
    background: var(--card-black);
    color: var(--ink-white);
    box-shadow: 0 10px 30px var(--card-shadow);
    display: flex;
    flex-direction: column;
    align-items: center;
  }
  .monogram {
    display: flex;
    align-items: center;
    justify-content: center;
    border: 2px solid var(--ink-white);
    border-radius: 50%;
    font-family: "Tinos", "Times New Roman", serif;
    color: var(--ink-white);
    font-weight: 400;
    letter-spacing: 0.02em;
  }
  /* Back side: enlarged mark only */
  .card--back { justify-content: center; }
  .card--back .monogram {
    width: 200px;
    height: 200px;
    font-size: 64px;
  }
  /* Front side: framed, small mark, name, contact */
  .card--front .frame {
    position: absolute;
    inset: 16px;
    border: 1.5px solid var(--frame-grey);
    pointer-events: none;
  }
  .card--front .monogram {
    margin-top: 74px;
    width: 92px;
    height: 92px;
    font-size: 30px;
  }
  .company-name {
    margin-top: 18px;
    font-family: "Pinyon Script", cursive;
    font-size: 44px;
    line-height: 1;
    font-weight: 400;
  }
  .contact {
    margin-top: 62px;
    font-family: "Tinos", "Times New Roman", serif;
    font-size: 18px;
    line-height: 1.3;
    text-align: center;
    font-style: normal;
  }
</style>
</head>
<body>
  <main class="canvas">
    <section class="card card--back" aria-label="Card back">
      <div class="monogram">MV</div>
    </section>

    <section class="card card--front" aria-label="Card front">
      <div class="frame"></div>
      <div class="monogram">MV</div>
      <h1 class="company-name">Margot Vallis Interiors</h1>
      <address class="contact">
        <p class="contact__mobile">Mobile: 0481 356 719</p>
        <p class="contact__email">Email: margotvallis@postlark.com</p>
      </address>
    </section>
  </main>
</body>
</html>
```